Schönheitssalon benötigt Flyer
Sehr schöne Arbeit, perfekt den Kundengeschmack getroffen. Leider zusätzliche Kosten durch (nicht enthaltene) Stockphotos, aber der Flyer ist sehr schick.
Zielgruppe
Ein Schönheitssalon in einer Pafümerie bietet diverse Angebote im Paket an (Gesichtsreinigung, Massage, Peeling, Maniküre, Sugaring). Vorrangig sollen Frauen angesprochen werden.
Aufgabenstellung
Faltblatt, gefalzt auf DIN A6 , 4-seiter
Endformat: 21,0 cm x 14,85 cm
gefalztes Endformat: 10,5 cm x 14,85 cm
Wir wünschen uns eine freundliche und helle Gestaltung mit rosé, voilett, pastell.
Das Grau, was jetzt gerade hinter dem Logo ist, wirkt sehr altbacken und nicht zeitgemäß.

```html
<!DOCTYPE html>
<html lang="de">
<head>
<meta charset="utf-8">
<title>Lichtblick Kosmetik – Faltblatt</title>
<link rel="stylesheet" href="https://fonts.googleapis.com/css2?family=Quicksand:wght@400;500;700&family=Parisienne&display=swap">
<style>
  :root {
    --backdrop: #e6daef;
    --paper: #fdfbfe;
    --violet: #8a5a9e;
    --violet-light: #b48bc4;
    --violet-deep: #6e3d84;
    --wash-1: #e9ddf0;
    --wash-2: #dccdea;
    --wash-3: #f3ecf7;
    --wash-blue: #dfe2f1;
    --rule: #e4d8ec;
  }
  * { box-sizing: border-box; margin: 0; padding: 0; }
  html, body { width: 1200px; height: 3600px; overflow: hidden; }
  body {
    background: var(--backdrop);
    font-family: "Quicksand", sans-serif;
    color: var(--violet);
    position: relative;
  }
  .spread {
    position: absolute;
    left: 80px;
    width: 1040px;
    height: 735px;
    background: var(--paper);
    display: flex;
    box-shadow: 0 6px 24px rgba(110, 61, 132, 0.18);
    overflow: hidden;
  }
  .spread--outside { top: 1005px; }
  .spread--inside { top: 1860px; }

  .wash {
    position: absolute; inset: 0;
    background:
      radial-gradient(ellipse 420px 300px at 28% 38%, var(--wash-2) 0%, transparent 70%),
      radial-gradient(ellipse 380px 280px at 72% 62%, var(--wash-1) 0%, transparent 70%),
      radial-gradient(ellipse 300px 220px at 85% 25%, var(--wash-blue) 0%, transparent 70%),
      radial-gradient(ellipse 360px 260px at 15% 80%, var(--wash-3) 0%, transparent 70%),
      var(--paper);
  }
  .wash--light { opacity: 0.45; }

  .panel {
    position: relative;
    width: 520px;
    height: 100%;
    padding: 60px 48px;
  }

  /* Outside: back panel */
  .intro { text-align: center; font-size: 16px; line-height: 1.45; }
  .intro p { margin-top: 30px; }
  .intro p:first-child { margin-top: 20px; }
  .intro strong { color: var(--violet-deep); font-weight: 700; }
  .portrait {
    position: absolute;
    left: 170px; top: 460px;
    width: 130px; height: 130px;
    border-radius: 50%;
    background: radial-gradient(circle at 50% 40%, #e9e4e8 0%, #b9b3b8 100%);
  }

  /* Outside: front panel */
  .front { text-align: center; }
  .brand { margin-top: 20px; display: flex; flex-direction: column; align-items: center; }
  .brand__dot {
    width: 46px; height: 46px; border-radius: 50%;
    border: 1.5px solid var(--violet);
  }
  .brand__name {
    margin-top: 14px;
    font-size: 38px; font-weight: 500;
    color: var(--violet-deep);
    letter-spacing: 0.5px;
  }
  .tagline {
    margin-top: 10px;
    font-family: "Parisienne", cursive;
    font-size: 34px;
    color: var(--violet-light);
  }
  .venue { margin-top: 44px; font-size: 15px; }
  .contact { margin-top: 90px; font-size: 15px; line-height: 1.35; }
  .contact .hours-title { margin-top: 14px; }

  /* Inside */
  .section-title {
    font-family: "Parisienne", cursive;
    font-size: 34px;
    color: var(--violet);
    font-weight: 400;
    border-bottom: 1px solid var(--rule);
    padding-bottom: 6px;
    margin-bottom: 22px;
  }
  .treatment { margin-bottom: 18px; }
  .treatment__head {
    display: flex; justify-content: space-between;
    font-size: 14px; font-weight: 500;
  }
  .treatment__price { display: flex; gap: 22px; }
  .treatment__price span:last-child { width: 48px; text-align: right; }
  .treatment__desc { font-size: 11px; line-height: 1.4; color: var(--violet-light); margin-top: 2px; }

  .price-table { width: 100%; border-collapse: collapse; font-size: 12.5px; }
  .price-table th { font-weight: 500; font-size: 11.5px; text-align: right; padding-bottom: 4px; }
  .price-table td { padding: 1.5px 0; }
  .price-table td.num { text-align: right; width: 62px; }
  .price-table .note td { padding-top: 3px; }
  .section-title--sub { margin-top: 26px; border-bottom: none; margin-bottom: 10px; font-size: 32px; }
</style>
</head>
<body>

<section class="spread spread--outside">
  <div class="wash"></div>

  <div class="panel back">
    <div class="intro">
      <p>Erleben Sie eine Auszeit und schalten<br>Sie einfach mal ab bei einer<br>Wohlfühl-Gesichtsbehandlung.</p>
      <p><strong>Ich biete Ihnen auf Sie zugeschnittene<br>Kosmetikprogramme auf höchstem Niveau<br>mit hochwertigen Produkten.</strong></p>
      <p>Sie brauchen einfach nur genießen!<br>Ich freue mich auf Sie!</p>
    </div>
    <div class="portrait" role="img" aria-label="Porträtfoto der Kosmetikerin"></div>
  </div>

  <div class="panel front">
    <div class="brand">
      <span class="brand__dot"></span>
      <span class="brand__name">Lichtblick Kosmetik</span>
    </div>
    <div class="tagline">Entspannung &amp; Kosmetik</div>
    <div class="venue">Im Haus der Stadt-Parfümerie Lindqvist</div>
    <div class="contact">
      <p>Musterstraße 120 a<br>12345 Musterstadt</p>
      <p class="hours-title">Öffnungszeiten</p>
      <p>Do.: 9.30 – 19.00 Uhr<br>Fr.: 9.30 – 19.00 Uhr</p>
    </div>
  </div>
</section>

<section class="spread spread--inside">
  <div class="wash wash--light"></div>

  <div class="panel">
    <h2 class="section-title">Gesichtsbehandlungen</h2>

    <div class="treatment">
      <div class="treatment__head"><span>Reinigungs-Behandlung:</span><span class="treatment__price"><span>ca. 60 Min.</span><span>35,- €</span></span></div>
      <div class="treatment__desc">Reinigung, Peeling, Ausreinigung, Maske &amp; Abschlusspflege</div>
    </div>
    <div class="treatment">
      <div class="treatment__head"><span>Basis-Behandlung:</span><span class="treatment__price"><span>ca. 90 Min.</span><span>49,- €</span></span></div>
      <div class="treatment__desc">Reinigung, Peeling, Ausreinigung, Augenbrauen-Korrektur,<br>Massage &amp; Maske, leichtes Make-Up auf Wunsch</div>
    </div>
    <div class="treatment">
      <div class="treatment__head"><span>Intensiv-Behandlung:</span><span class="treatment__price"><span>ca. 90 Min.</span><span>59,- €</span></span></div>
      <div class="treatment__desc">Reinigung, Peeling, Ausreinigung, Augenbrauen-Korrektur,<br>Ampulle/Massage, Maske &amp; Augenmaske, leichtes Make-Up<br>auf Wunsch</div>
    </div>
    <div class="treatment">
      <div class="treatment__head"><span>Verwöhn-Behandlung:</span><span class="treatment__price"><span>ca. 90 Min.</span><span>67,- €</span></span></div>
      <div class="treatment__desc">Reinigung, Peeling, Ausreinigung, Augenbrauen-Korrektur, Ampulle,<br>Massage, Maske, Hals- &amp; Dekolleté-Behandlung, leichtes Make-Up<br>auf Wunsch</div>
    </div>
    <div class="treatment">
      <div class="treatment__head"><span>Luxus-Behandlung:</span><span class="treatment__price"><span>ca. 120 Min.</span><span>81,- €</span></span></div>
      <div class="treatment__desc">Reinigung, Peeling, Ausreinigung, Augenbrauen-Korrektur,<br>Ampulle, Massage, Vlies-Maske, Augenmaske, Lippenpackung,<br>Handmassage &amp; Hals- &amp; Dekolleté-Behandlung, leichtes<br>Make-Up auf Wunsch</div>
    </div>
    <div class="treatment">
      <div class="treatment__head"><span>Teenie-Behandlung (bis 18 Jahre):</span><span class="treatment__price"><span>ca. 60 Min.</span><span>28,- €</span></span></div>
      <div class="treatment__desc">Reinigung, Peeling, Ausreinigung &amp; Maske</div>
    </div>
  </div>

  <div class="panel">
    <h2 class="section-title">Zusatz- &amp; Einzelbehandlungen</h2>
    <table class="price-table">
      <thead><tr><th></th><th>zusätzlich</th><th>einzeln</th></tr></thead>
      <tbody>
        <tr><td>Augenbrauen zupfen/waxen</td><td class="num"></td><td class="num">8,- €</td></tr>
        <tr><td>Augenbrauen färben</td><td class="num">6,50 €</td><td class="num">8,50 €</td></tr>
        <tr><td>Wimpern färben</td><td class="num">7,- €</td><td class="num">9,- €</td></tr>
        <tr><td>Augenbrauen &amp; Wimpern färben + zupfen</td><td class="num"></td><td class="num">21,- €</td></tr>
        <tr><td>Wimpernwelle</td><td class="num">22,- €</td><td class="num">32,- €</td></tr>
        <tr><td>Pflegende Maniküre (60 Min.)</td><td class="num">18,- €</td><td class="num">26,- €</td></tr>
        <tr><td>Pflegende Maniküre + Lack</td><td class="num">24,- €</td><td class="num">32,- €</td></tr>
        <tr><td>Wirkstoffampulle</td><td class="num"></td><td class="num">9,- €</td></tr>
        <tr><td>Tages-Make-Up</td><td class="num"></td><td class="num">13,- €</td></tr>
        <tr><td>Abend- / Foto-Make-Up</td><td class="num"></td><td class="num">35,- €</td></tr>
        <tr><td>Braut-Make-Up (inkl. Probe)</td><td class="num"></td><td class="num">70,- €</td></tr>
        <tr><td>Klassische Rückenmassage ca. 30 Min.</td><td class="num"></td><td class="num">25,- €</td></tr>
      </tbody>
    </table>

    <h2 class="section-title section-title--sub">Sugaring</h2>
    <table class="price-table">
      <tbody>
        <tr><td>Oberlippe</td><td class="num">9,- €</td><td class="num"></td></tr>
        <tr><td>Oberlippe + Kinn</td><td class="num">14,- €</td><td class="num"></td></tr>
        <tr><td>Arme</td><td class="num">ab 25,- €</td><td class="num"></td></tr>
        <tr><td>Beine Unterschenkel</td><td class="num">23,- €</td><td class="num"></td></tr>
        <tr><td>Beine komplett</td><td class="num">39,- €</td><td class="num"></td></tr>
        <tr><td>Rücken</td><td class="num">ab 35,- €</td><td class="num"></td></tr>
        <tr class="note"><td colspan="3">Andere Bereiche auf Anfrage!</td></tr>
      </tbody>
    </table>
  </div>
</section>

</body>
</html>
```